Business Card Design Project

We require a business card template to cover basic contact information - our company logo, names of employees, title, mobile and email.

Target Market(s)

Corporate

Industry/Entity Type

Business

Font styles to use
Sans Serif

Requirements
Nice to have
• Thinking it would be great just to have the logo taking up approximately half the space (so it goes as far across the top of the card as possible) and then contact details in the lower half of the card. Keen just to use only the two colours in the logo, on a white background.
Should not have
• No fussy drawings

```html
<!DOCTYPE html>
<html lang="en">
<head>
<meta charset="utf-8">
<title>Brightmere Business Card</title>
<link rel="stylesheet" href="https://fonts.googleapis.com/css2?family=Source+Sans+3:wght@400;500&display=swap">
<style>
  :root {
    --teal: #4dd6c1;
    --blue: #2a6de6;
    --ink: #2e3438;
    --bg-centre: #f4fdfd;
    --bg-edge: #d8f3f7;
    --band-top: #58cbfa;
    --band-bottom: #1e74df;
    --white: #ffffff;
  }
  html, body {
    margin: 0;
    padding: 0;
    width: 1200px;
    height: 686px;
    overflow: hidden;
  }
  .card {
    position: relative;
    width: 1200px;
    height: 686px;
    overflow: hidden;
    background: radial-gradient(ellipse 70% 75% at 68% 40%, var(--bg-centre) 0%, var(--bg-edge) 100%);
    font-family: "Source Sans 3", sans-serif;
  }
  .employee {
    position: absolute;
    left: 82px;
    top: 54px;
    text-align: center;
  }
  .employee-name {
    margin: 0;
    font-size: 56px;
    font-weight: 400;
    line-height: 1;
    letter-spacing: 0.5px;
  }
  .employee-name .first { color: var(--teal); }
  .employee-name .last { color: var(--blue); }
  .employee-title {
    margin: 22px 0 0;
    font-size: 40px;
    font-weight: 400;
    color: var(--ink);
    line-height: 1;
  }
  .company-name {
    position: absolute;
    right: 112px;
    top: 196px;
    margin: 0;
    font-size: 132px;
    font-weight: 400;
    line-height: 1;
    color: var(--teal);
    letter-spacing: -1px;
  }
  .contact-band {
    position: absolute;
    left: 0;
    top: 412px;
    width: 1200px;
    height: 160px;
  }
  .contact {
    position: absolute;
    top: 466px;
    display: flex;
    align-items: center;
    gap: 10px;
    color: var(--white);
    font-size: 35px;
    font-weight: 400;
    line-height: 1;
  }
  .contact-phone { left: 56px; }
  .contact-email { right: 58px; }
  .contact svg { display: block; }
</style>
</head>
<body>
<div class="card">
  <div class="employee">
    <h1 class="employee-name"><span class="first">Emp</span> <span class="last">Name</span></h1>
    <p class="employee-title">Title</p>
  </div>

  <p class="company-name">Brightmere</p>

  <svg class="contact-band" width="1200" height="160" viewBox="0 0 1200 160" aria-hidden="true">
    <defs>
      <linearGradient id="bandFill" x1="0" y1="0" x2="0" y2="1">
        <stop offset="0" stop-color="var(--band-top)"/>
        <stop offset="1" stop-color="var(--band-bottom)"/>
      </linearGradient>
      <radialGradient id="bandShadow" cx="0.5" cy="0.5" r="0.5">
        <stop offset="0" stop-color="#000" stop-opacity="0.75"/>
        <stop offset="1" stop-color="#000" stop-opacity="0"/>
      </radialGradient>
    </defs>
    <ellipse cx="590" cy="140" rx="470" ry="9" fill="url(#bandShadow)"/>
    <path d="M0 26 H950 C965 26 972 6 983 4 C994 6 1001 26 1016 26 H1200 V134 H0 Z" fill="url(#bandFill)"/>
  </svg>

  <div class="contact contact-phone">
    <svg width="42" height="42" viewBox="0 0 42 42" aria-hidden="true">
      <circle cx="21" cy="21" r="18" fill="none" stroke="var(--white)" stroke-width="2.5"/>
      <path d="M16 11 C13 13 12 17 14 22 C16 27 19 31 24 32 L27 29 L23 25 L21 27 C19 25 18 22 17 19 L19 17 L16 11 Z" fill="var(--white)"/>
    </svg>
    <span>123-456-7890</span>
  </div>

  <div class="contact contact-email">
    <svg width="44" height="30" viewBox="0 0 44 30" aria-hidden="true">
      <rect x="1.5" y="1.5" width="41" height="27" fill="var(--white)" stroke="#cfe4f7" stroke-width="1.5"/>
      <path d="M2 2 L22 17 L42 2" fill="none" stroke="#9fc4e8" stroke-width="2"/>
      <path d="M2 28 L17 13 M42 28 L27 13" fill="none" stroke="#9fc4e8" stroke-width="1.5"/>
    </svg>
    <span>name@brightmere.com</span>
  </div>
</div>
</body>
</html>
```